Harlow Custom Craft Website update

I would like an updated website to my current site (Harlowcraft.com).
I have an updated logo i would like to incorporate.
24 pages , would like to integrate videos of the boats (that i can upload later)

Target Market(s)

Professional and Commercial boat owners

Industry/Entity Type

Custom Boat Manufacturing

Coding

Coded - Design and coding required

Number of Pages Required

5+ page

Font styles to use
Serif

Requirements
Must have
• Easy to read, well laid-out, and video integration
Nice to have
• Fresh up to date look

```html
<!DOCTYPE html>
<html lang="en">
<head>
<meta charset="utf-8">
<title>Harlow Custom Craft – Our Boats &amp; Product Page</title>
<link rel="stylesheet" href="https://fonts.googleapis.com/css2?family=Manrope:wght@400;500;600;700;800&display=swap">
<style>
:root{
  --navy:#00449a;
  --blue-link:#1a5fd0;
  --red:#d0152e;
  --red-bright:#e02128;
  --ink:#1b1f2a;
  --muted:#7b808a;
  --line:#e6e6e6;
  --paper:#ffffff;
  --mist:#f4f4f4;
  --sand:#f6f2ee;
  --star:#f5b400;
  --star-off:#d4d4d4;
}
*{margin:0;padding:0;box-sizing:border-box}
html,body{width:1200px;height:1200px;overflow:hidden;background:var(--paper)}
body{font-family:"Manrope",sans-serif;color:var(--ink)}
.board{position:absolute;left:0;top:0;width:1932px;height:1932px;transform:scale(0.62112);transform-origin:0 0}
.page{position:absolute;top:0;height:1932px;overflow:hidden;background:var(--paper)}
.page--shop{left:0;width:1000px}
.page--product{left:1194px;width:738px}
.abs{position:absolute;line-height:1;white-space:nowrap}
.brand{font-weight:800;color:var(--navy);letter-spacing:-.3px}
.photo{position:absolute;border-radius:4px;background:linear-gradient(180deg,#5fb2ef 0%,#a9dcf5 40%,#3cb9c7 62%,#1f8fa6 100%)}
.photo--marina{background:linear-gradient(180deg,#e9f1f5 0%,#b9cfdd 45%,#4d7890 70%,#2e556c 100%)}
.photo--deck{background:linear-gradient(180deg,#d8dde2 0%,#a3b3c0 60%,#7d8d99 100%)}
.photo--cabin{background:linear-gradient(180deg,#e9e2dc 0%,#a36b5a 55%,#5a3a33 100%)}
.heart{position:absolute;width:22px;height:22px;border-radius:4px;background:#fff;display:flex;align-items:center;justify-content:center}
.stars{color:var(--star);letter-spacing:1px}
.stars .off{color:var(--star-off)}
.nav a{color:var(--ink);text-decoration:none;font-weight:500}
/* shop page */
.hero-title{font-size:44px;font-weight:500;color:#fff;left:0;width:1000px;text-align:center}
.crumb{font-size:11px;color:#fff;left:0;width:1000px;text-align:center;font-weight:500}
.side-head{font-size:14px;font-weight:600}
.side-dash{width:11px;height:1px;background:#888}
.cat{font-size:11.5px;color:var(--ink)}
.cat--active{color:var(--blue-link)}
.check{position:absolute;width:13px;height:13px;border:1px solid #cfcfcf;border-radius:2px}
.card-title{font-size:14px;font-weight:500}
.card-price{font-size:13px;color:var(--muted)}
/* footer */
.foot-tag{color:#fff;font-weight:500;white-space:normal}
.foot-head{color:var(--red)}
.foot-txt{color:#fff}
.u{border-bottom:1px solid #fff;padding-bottom:2px}
/* product */
.small{font-size:7.5px;color:var(--muted)}
.desc-list{position:absolute;left:42px;font-size:7.5px;color:var(--muted);line-height:14.7px}
.acc-line{position:absolute;left:42px;width:655px;height:1px;background:var(--line)}
.acc-head{font-size:12px;font-weight:500}
.pay{position:absolute;top:470px;width:26px;height:19px;border:1px solid var(--line);border-radius:3px;background:#fff}
.pay i{position:absolute;left:7px;top:6px;width:11px;height:6px;border-radius:1px;background:var(--navy)}
</style>
</head>
<body>
<div class="board">

<!-- ================= SHOP PAGE ================= -->
<section class="page page--shop">
  <header>
    <div class="abs brand" style="left:48px;top:28px;font-size:24px">Harlow Custom Craft</div>
    <nav class="nav abs" style="left:361px;top:35px;font-size:13px">
      <a href="#">Home</a>&nbsp;&nbsp;&nbsp;&nbsp;&nbsp;<a href="#">About Us</a>&nbsp;&nbsp;&nbsp;&nbsp;&nbsp;<a href="#">⊙ Our Boats</a>&nbsp;&nbsp;&nbsp;&nbsp;&nbsp;<a href="#">Links</a>&nbsp;&nbsp;&nbsp;&nbsp;&nbsp;<a href="#">News</a>
    </nav>
    <svg class="abs" style="left:857px;top:31px" width="20" height="22" viewBox="0 0 20 22" fill="none" stroke="#1b1f2a" stroke-width="1.5"><path d="M3 7h12v13H3z"/><path d="M6 7V5a3 3 0 0 1 6 0v2"/><circle cx="15" cy="16" r="4" fill="#00449a" stroke="none"/></svg>
    <svg class="abs" style="left:896px;top:32px" width="20" height="20" viewBox="0 0 20 20" fill="none" stroke="#1b1f2a" stroke-width="1.8"><circle cx="9" cy="9" r="7"/><path d="M14 14l5 5"/></svg>
    <svg class="abs" style="left:936px;top:33px" width="16" height="16" viewBox="0 0 16 16" fill="#1b1f2a"><circle cx="2" cy="2" r="2"/><circle cx="8" cy="2" r="2"/><circle cx="14" cy="2" r="2"/><circle cx="2" cy="8" r="2"/><circle cx="8" cy="8" r="2"/><circle cx="14" cy="8" r="2"/><circle cx="2" cy="14" r="2"/><circle cx="8" cy="14" r="2"/><circle cx="14" cy="14" r="2"/></svg>
  </header>

  <svg class="abs" style="left:0;top:92px" width="1000" height="200" viewBox="0 0 1000 200">
    <rect width="1000" height="200" fill="var(--navy)"/>
    <path d="M0 130 C80 108 150 96 220 102 C330 112 420 200 560 196 C700 192 800 120 880 132 C940 140 975 160 1000 170 L1000 200 L0 200Z" fill="#fff"/>
  </svg>
  <h1 class="abs hero-title" style="top:159px">Our Boats</h1>
  <div class="abs crumb" style="top:211px">Home&nbsp; / &nbsp;Our Boats</div>

  <aside>
    <div class="abs side-head" style="left:44px;top:375px">Filter by category</div>
    <div class="abs side-dash" style="left:215px;top:382px"></div>
    <div class="abs cat cat--active" style="left:44px;top:409px">All categories</div>
    <div class="abs cat" style="left:55px;top:432px;line-height:22.55px">
      Uncategorized<br>26' Dive Special<br>26' Sport Fish<br>31' Dive Special<br>31' Enforcer<br>32' Sport Fish<br>36' Dive Special<br>36' Glass Bottom Boat<br>36' Research Vessel<br>36' Search &amp; Rescue<br>42' Dive Special<br>46' Research Vessel<br>46' Search &amp; Rescue<br>46' Sport Fish<br>53' Dive/Excursion<br>53' Sport Fish<br>58' Dive Special<br>71' Custom Dive<br>Optional Equipment<br>US Coast Guard Package
    </div>

    <div class="abs side-head" style="left:45px;top:910px;font-size:13px">Price</div>
    <div class="abs side-dash" style="left:212px;top:917px"></div>
    <div class="abs" style="left:48px;top:944px;width:172px;height:2px;background:#1a7fc2"></div>
    <div class="abs" style="left:45px;top:942px;width:6px;height:6px;border-radius:50%;background:var(--ink)"></div>
    <div class="abs" style="left:217px;top:942px;width:6px;height:6px;border-radius:50%;background:var(--ink)"></div>
    <div class="abs" style="left:45px;top:952px;font-size:10px;color:var(--muted)">110</div>
    <div class="abs" style="left:203px;top:952px;font-size:10px;color:var(--muted)">660</div>
    <div class="abs" style="left:45px;top:969px;font-size:11px;color:var(--muted)">Price: <span style="color:var(--ink)">110 - 660</span></div>

    <div class="abs side-head" style="left:45px;top:1015px;font-size:13px">Rating</div>
    <div class="abs side-dash" style="left:212px;top:1022px"></div>
    <div class="check" style="left:45px;top:1046px"></div><div class="abs" style="left:65px;top:1048px;font-size:9px;letter-spacing:2px">★★★★★</div>
    <div class="check" style="left:45px;top:1066px"></div><div class="abs" style="left:65px;top:1068px;font-size:9px;letter-spacing:2px">★★★★<span style="color:var(--star-off)">★</span></div>
    <div class="check" style="left:45px;top:1085px"></div><div class="abs" style="left:65px;top:1087px;font-size:9px;letter-spacing:2px">★★★<span style="color:var(--star-off)">★★</span></div>
    <div class="check" style="left:45px;top:1105px"></div><div class="abs" style="left:65px;top:1107px;font-size:9px;letter-spacing:2px">★★<span style="color:var(--star-off)">★★★</span></div>
    <div class="check" style="left:45px;top:1124px"></div><div class="abs" style="left:65px;top:1126px;font-size:9px;letter-spacing:2px">★<span style="color:var(--star-off)">★★★★</span></div>
  </aside>

  <main>
    <div class="abs" style="left:254px;top:376px;font-size:13.5px;color:var(--muted)">Showing all 2 results</div>
    <div class="abs" style="left:790px;top:376px;font-size:13.5px">Sort by latest</div>
    <svg class="abs" style="left:950px;top:380px" width="9" height="6" viewBox="0 0 9 6" fill="none" stroke="#1b1f2a" stroke-width="1.5"><path d="M1 1l3.5 3.5L8 1"/></svg>

    <div class="photo" role="img" aria-label="Custom dive boat on turquoise water" style="left:254px;top:411px;width:161px;height:161px"></div>
    <div class="heart" style="left:381px;top:423px"><svg width="12" height="11" viewBox="0 0 12 11" fill="none" stroke="#333" stroke-width="1.2"><path d="M6 10S1 7 1 3.5A2.5 2.5 0 0 1 6 2.5 2.5 2.5 0 0 1 11 3.5C11 7 6 10 6 10z"/></svg></div>
    <div class="photo photo--marina" role="img" aria-label="Dive special yacht moored at a marina" style="left:435px;top:411px;width:161px;height:161px"></div>
    <div class="heart" style="left:562px;top:423px"><svg width="12" height="11" viewBox="0 0 12 11" fill="none" stroke="#333" stroke-width="1.2"><path d="M6 10S1 7 1 3.5A2.5 2.5 0 0 1 6 2.5 2.5 2.5 0 0 1 11 3.5C11 7 6 10 6 10z"/></svg></div>

    <div class="abs card-title" style="left:254px;top:586px">71’ Custom Dive</div>
    <div class="abs card-price" style="left:254px;top:609px">$114.000 – $118.000</div>
    <div class="abs stars" style="left:254px;top:627px;font-size:10px">★★★★★</div>
    <div class="abs card-title" style="left:435px;top:586px">58’ Dive Special</div>
    <div class="abs card-price" style="left:435px;top:609px">$655.000</div>
    <div class="abs stars" style="left:435px;top:627px;font-size:10px">★★★★<span class="off">★</span></div>
  </main>

  <footer>
    <svg class="abs" style="left:0;top:1300px" width="1000" height="632" viewBox="0 0 1000 632">
      <rect width="1000" height="632" fill="var(--mist)"/>
      <path d="M0 48 C150 30 300 0 420 4 C560 10 640 50 760 68 C860 82 940 80 1000 78 L1000 490 L0 490Z" fill="var(--navy)"/>
      <rect y="490" width="1000" height="142" fill="var(--red)"/>
    </svg>
    <div class="abs brand" style="left:56px;top:1440px;font-size:38px;color:#fff">Harlow Custom Craft</div>
    <p class="abs foot-tag" style="left:56px;top:1512px;width:470px;font-size:24px;line-height:26px">Harlow Craft uses the latest technology and only the highest quality materials to build our custom boats.</p>

    <div class="abs foot-head" style="left:56px;top:1645px;font-size:13.5px">Address</div>
    <div class="abs foot-txt" style="left:56px;top:1680px;font-size:12.5px;line-height:19.5px">Harlow Craft, Inc. 4820<br>Harbor Rd. Bayport, LA 70999<br>USA</div>
    <div class="abs foot-head" style="left:283px;top:1645px;font-size:13.5px">Say Hello</div>
    <div class="abs foot-txt" style="left:283px;top:1680px;font-size:12.5px"><span class="u">office@harlowcraft.com</span></div>
    <div class="abs foot-txt" style="left:283px;top:1711px;font-size:13px;font-weight:500">+1 (555) 014-2290</div>
    <div class="abs foot-head" style="left:510px;top:1645px;font-size:13.5px">Social Media</div>
    <div class="abs foot-txt" style="left:512px;top:1680px;font-size:12.5px">●&nbsp;&nbsp; Friendbook</div>
    <div class="abs foot-txt" style="left:516px;top:1709px;font-size:12.5px">◻&nbsp; <span class="u">Snapfeed</span></div>
    <div class="abs foot-head" style="left:737px;top:1645px;font-size:13.5px">Newsletter</div>
    <svg class="abs" style="left:737px;top:1684px" width="13" height="10" viewBox="0 0 13 10" fill="none" stroke="#fff" stroke-width="1"><rect x=".5" y=".5" width="12" height="9"/><path d="M.5 .5l6 5 6-5"/></svg>
    <div class="abs foot-txt" style="left:755px;top:1683px;font-size:12px">Enter Your Email Address</div>
    <div class="abs" style="left:901px;top:1683px;width:14px;height:12px;border-radius:2px;background:var(--red)"></div>
    <svg class="abs" style="left:930px;top:1684px" width="14" height="10" viewBox="0 0 14 10" fill="none" stroke="#fff" stroke-width="1.5"><path d="M0 5h12M8 1l4 4-4 4"/></svg>
    <div class="abs" style="left:737px;top:1712px;width:206px;height:1px;background:rgba(255,255,255,.3)"></div>
    <div class="abs" style="left:737px;top:1731px;width:10px;height:10px;border:1px solid rgba(255,255,255,.7);border-radius:2px"></div>
    <div class="abs" style="left:754px;top:1732px;font-size:9.5px;color:rgba(255,255,255,.8)">I agree to the <span style="text-decoration:underline;color:#fff">Privacy Policy</span></div>

    <div class="abs" style="left:56px;top:1838px;width:887px;height:1px;background:rgba(255,255,255,.7)"></div>
    <div class="abs" style="left:56px;top:1860px;font-size:14px;color:#fff"><span style="color:var(--blue-link)">Harlow Craft, Inc.</span> © 2025. All rights reserved.</div>
  </footer>
</section>

<!-- ================= PRODUCT PAGE ================= -->
<section class="page page--product">
  <header>
    <div class="abs brand" style="left:36px;top:22px;font-size:15px">Harlow Custom Craft</div>
    <nav class="nav abs" style="left:266px;top:23px;font-size:8px">
      <a href="#">Home</a>&nbsp;&nbsp;&nbsp;&nbsp;<a href="#">About Us</a>&nbsp;&nbsp;&nbsp;&nbsp;<a href="#">⊙ Our Boats</a>&nbsp;&nbsp;&nbsp;&nbsp;<a href="#">Links</a>&nbsp;&nbsp;&nbsp;&nbsp;<a href="#">News</a>
    </nav>
    <svg class="abs" style="left:634px;top:21px" width="12" height="13" viewBox="0 0 20 22" fill="none" stroke="#1b1f2a" stroke-width="1.8"><path d="M3 7h12v13H3z"/><path d="M6 7V5a3 3 0 0 1 6 0v2"/><circle cx="15" cy="16" r="4" fill="#00449a" stroke="none"/></svg>
    <svg class="abs" style="left:662px;top:22px" width="12" height="12" viewBox="0 0 20 20" fill="none" stroke="#1b1f2a" stroke-width="2.2"><circle cx="9" cy="9" r="7"/><path d="M14 14l5 5"/></svg>
    <svg class="abs" style="left:691px;top:22px" width="10" height="10" viewBox="0 0 16 16" fill="#1b1f2a"><circle cx="2" cy="2" r="2"/><circle cx="8" cy="2" r="2"/><circle cx="14" cy="2" r="2"/><circle cx="2" cy="8" r="2"/><circle cx="8" cy="8" r="2"/><circle cx="14" cy="8" r="2"/><circle cx="2" cy="14" r="2"/><circle cx="8" cy="14" r="2"/><circle cx="14" cy="14" r="2"/></svg>
  </header>
  <div class="abs" style="left:0;top:64px;width:738px;height:35px;background:var(--sand)"></div>
  <div class="abs" style="left:0;top:78px;width:738px;text-align:center;font-size:8px;font-weight:500">GET 10% OFF YOUR FIRST PURCHASE</div>
  <div class="abs" style="left:220px;top:76px;font-size:10px;color:var(--muted)">‹</div>
  <div class="abs" style="left:513px;top:76px;font-size:10px;color:var(--muted)">›</div>

  <div class="photo" role="img" aria-label="Boat thumbnail on blue water" style="left:42px;top:161px;width:61px;height:61px"></div>
  <div class="photo photo--deck" role="img" aria-label="Boat thumbnail beside a dock" style="left:42px;top:232px;width:61px;height:61px"></div>
  <div class="photo photo--marina" role="img" aria-label="Boat thumbnail side view" style="left:42px;top:303px;width:61px;height:61px"></div>
  <div class="photo photo--cabin" role="img" aria-label="Boat interior salon thumbnail" style="left:42px;top:374px;width:61px;height:61px"></div>
  <div class="photo" role="img" aria-label="71 foot custom dive boat cruising on turquoise water" style="left:118px;top:161px;width:290px;height:289px"></div>

  <div class="abs small" style="left:439px;top:161px;font-size:7px">Home / 71’ Custom Dive / 71’ Custom Dive</div>
  <h2 class="abs" style="left:439px;top:184px;font-size:17px;font-weight:500">71’ Custom Dive</h2>
  <div class="abs" style="left:439px;top:213px;font-size:12px;font-weight:500">$114.000 – $118.000</div>
  <div class="abs stars" style="left:651px;top:215px;font-size:7px">★★★★★</div>
  <p class="abs small" style="left:439px;top:246px;width:258px;white-space:normal;line-height:14.6px">The “New” Harlow 71’ x 18’ model is now available and the custom possibilities are endless. With over 252 square feet in the salon area and over 240 square feet below, there will be plenty of room for all the amenities you desire.</p>
  <p class="abs small" style="left:439px;top:319px;width:258px;white-space:normal;line-height:14.6px">No matter if you are diving and/or fishing, over 420 square feet of deck space will give you and your clients enough room for necessary equipment with plenty of space for mobility.</p>

  <div class="abs" style="left:439px;top:399px;width:66px;height:27px;border:1px solid var(--line);border-radius:3px"></div>
  <div class="abs small" style="left:453px;top:409px">1</div>
  <div class="abs small" style="left:485px;top:404px;font-size:6px;line-height:8px">⌃<br>⌄</div>
  <div class="abs" style="left:510px;top:399px;width:73px;height:27px;border-radius:3px;background:#c9ccd2"></div>
  <div class="abs" style="left:524px;top:409px;font-size:7px;color:#fff">▢ Buy now</div>
  <div class="abs" style="left:587px;top:399px;width:28px;height:27px;border:1px solid var(--line);border-radius:3px"></div>
  <svg class="abs" style="left:596px;top:408px" width="10" height="9" viewBox="0 0 12 11" fill="none" stroke="#333" stroke-width="1.2"><path d="M6 10S1 7 1 3.5A2.5 2.5 0 0 1 6 2.5 2.5 2.5 0 0 1 11 3.5C11 7 6 10 6 10z"/></svg>

  <div class="abs" style="left:439px;top:448px;font-size:8px;font-weight:500">Guaranteed safe checkout</div>
  <div class="pay" style="left:439px"><i></i></div>
  <div class="pay" style="left:470px"><i></i></div>
  <div class="pay" style="left:501px"><i></i></div>
  <div class="pay" style="left:532px"><i></i></div>

  <div class="abs" style="left:439px;top:510px;width:258px;height:46px;border-radius:4px;background:var(--sand)"></div>
  <svg class="abs" style="left:449px;top:524px" width="20" height="18" viewBox="0 0 20 18" fill="none" stroke="#888" stroke-width="1.2"><path d="M3 11V8a7 7 0 0 1 14 0v3"/><rect x="1" y="10" width="4" height="6" rx="1"/><rect x="15" y="10" width="4" height="6" rx="1"/></svg>
  <div class="abs" style="left:477px;top:522px;font-size:7.5px;color:#444">Need Help? Call Us <b style="color:var(--ink)">+1 555 201 77 40</b></div>
  <div class="abs" style="left:477px;top:537px;font-size:7.5px;color:#444">Monday - Friday 9:00 - 17:00</div>

  <div class="abs acc-head" style="left:42px;top:599px">Description</div>
  <div class="abs" style="left:688px;top:598px;font-size:10px">⌃</div>
  <div class="abs small" style="left:42px;top:628px">This model was custom built to our clients exact specifications. It included basic specs from our 46’ model in addition to the following optional items:</div>
  <div class="desc-list" style="top:654px">
    4 bank battery charger Pilot House with two (2) bunks<br>
    2nd Controls aft top rail 4 bunks in lower forward cabin<br>
    (2) Brauner compressors 2 larger bunks lower starboard side<br>
    9 Cascadia system 2 bunks lower port side<br>
    8’ x 8’ ice hold 2 heads &amp; showers in lower cabin<br>
    Veltra 4210 bow and stern thruster Teak floor in cabin<br>
    300lb ice maker Television<br>
    40kw Kolmar 3 phase gen set Engine room fan vent system<br>
    4 Marine air conditioning units 2 Steadykeel 0-High Speed Stabilizers<br>
    Bench style seating throughout cabin Salon table and bar with stools<br>
    Removable decompression chamber Head &amp; shower on main deck<br>
    Plotter, sounder, transceiver, radar Auto pilot<br>
    900 gallon fuel tanks<br>
    Ravin Atlas Marine heads<br>
    Sound proofing around engine room<br>
    Veltra anchor windlass / 24v DC<br>
    Side boarding doors aft port, &amp; starboard<br>
    Microwave, refrigerator, and stove top for 24vt system
  </div>
  <div class="desc-list" style="top:932px">Customer’s power choice:<br>(2) 1136 hp Marlow M18 Diesel engines</div>

  <div class="acc-line" style="top:973px"></div>
  <div class="abs acc-head" style="left:42px;top:988px">Delivery Info</div>
  <div class="abs" style="left:688px;top:987px;font-size:10px">⌄</div>
  <div class="acc-line" style="top:1014px"></div>
  <div class="abs acc-head" style="left:42px;top:1029px">Reviews (1)</div>
  <div class="abs" style="left:688px;top:1028px;font-size:10px">⌄</div>
  <div class="acc-line" style="top:1054px"></div>

  <h3 class="abs" style="left:42px;top:1093px;font-size:24px;font-weight:500">Related products</h3>
  <div class="photo photo--marina" role="img" aria-label="58 foot dive special yacht at a marina" style="left:42px;top:1145px;width:208px;height:207px"></div>
  <div class="abs" style="left:42px;top:1368px;font-size:9px;font-weight:500">58’ Dive Special</div>
  <div class="abs" style="left:42px;top:1384px;font-size:9px;color:var(--muted)">$655.000</div>
  <div class="abs stars" style="left:42px;top:1400px;font-size:7px">★★★★<span class="off">★</span></div>

  <footer>
    <svg class="abs" style="left:0;top:1470px" width="738" height="462" viewBox="0 0 738 462">
      <path d="M0 36 C80 20 150 8 210 10 C320 14 420 40 520 52 C620 62 690 60 738 58 L738 370 L0 370Z" fill="var(--navy)"/>
      <rect y="370" width="738" height="92" fill="var(--red-bright)"/>
    </svg>
    <div class="abs brand" style="left:42px;top:1583px;font-size:26px;color:#fff">Harlow Custom Craft</div>
    <p class="abs foot-tag" style="left:42px;top:1634px;width:350px;font-size:17px;line-height:19px">Harlow Craft uses the latest technology and only the highest quality materials to build our custom boats.</p>

    <div class="abs foot-head" style="left:42px;top:1732px;font-size:9px">Address</div>
    <div class="abs foot-txt" style="left:42px;top:1758px;font-size:8px;line-height:13.5px">Harlow Craft, Inc. 4820<br>Harbor Rd. Bayport, LA 70999<br>USA</div>
    <div class="abs foot-head" style="left:209px;top:1732px;font-size:9px">Say Hello</div>
    <div class="abs foot-txt" style="left:209px;top:1758px;font-size:8px"><span class="u">office@harlowcraft.com</span></div>
    <div class="abs foot-txt" style="left:209px;top:1781px;font-size:8.5px;font-weight:500">+1 (555) 014-2290</div>
    <div class="abs foot-head" style="left:376px;top:1732px;font-size:9px">Social Media</div>
    <div class="abs foot-txt" style="left:376px;top:1758px;font-size:8px">●&nbsp; Friendbook</div>
    <div class="abs foot-txt" style="left:376px;top:1779px;font-size:8px">◻&nbsp; Snapfeed</div>
    <div class="abs foot-head" style="left:544px;top:1732px;font-size:9px">Newsletter</div>
    <div class="abs foot-txt" style="left:544px;top:1760px;font-size:7.5px">✉ Enter Your Email Address</div>
    <div class="abs" style="left:664px;top:1759px;width:10px;height:8px;border-radius:1px;background:var(--red)"></div>
    <div class="abs foot-txt" style="left:686px;top:1758px;font-size:10px">→</div>
    <div class="abs" style="left:544px;top:1780px;width:153px;height:1px;background:rgba(255,255,255,.3)"></div>
    <div class="abs" style="left:544px;top:1796px;width:7px;height:7px;border:1px solid rgba(255,255,255,.7);border-radius:1px"></div>
    <div class="abs" style="left:556px;top:1797px;font-size:6px;color:rgba(255,255,255,.8)">I agree to the <span style="text-decoration:underline;color:#fff">Privacy Policy</span></div>

    <div class="abs" style="left:42px;top:1875px;width:655px;height:1px;background:rgba(255,255,255,.7)"></div>
    <div class="abs" style="left:42px;top:1891px;font-size:9.5px;color:#fff"><span style="color:var(--blue-link)">Harlow Craft, Inc.</span> © 2025. All rights reserved.</div>
  </footer>
</section>

</div>
</body>
</html>
```